Dog Grooming Provisions - Fur Refresher Spray *

We are Willow Bend Meadows. A city dog's country camp. We are a dog services company providing a camp experience in Upstate NY to the dogs of NYC. We are creating a hand made fur refresher spray for our clients (who are dogs!) for the holidays.
These labels will be used on a 4 ounce vintage style spray bottles. The design should have a vintage grooming provisions feel. We'd like to see the design be a simple, vintage style black with white, charcoal, or very dark almost black green.
The design should incorporate our varying vintage fonts, our logo with "grooming provisions" all natural & handmade, Fur Refresh
Obviously this is a gift and while Fur Refresh is important, our brand should be a focus. Perhaps a very simple and "elegant" bone but steer away from paws and pet cheesy! Classic, vintage and camp.

Target Market(s)

Upscale Pet Owners of NYC

Industry/Entity Type

Pet Care

Logo Text

Willow Bend Meadows Dog Camp (Dog Camp is is for logo not necessary for label)

Font styles to use
Serif
Sans Serif
Script

Colors
9bcb3b
000000
5c5c5c

Requirements
Must have
• I am looking for a black and white or very simple design. I'd even like our logo for this use be black/white (if possible? - not sure if that can happen?)
• Our branding! Simple vintage feel.
• Grooming Provisions
• Fur Refresher or Fur Refresh or Fur Fresh Spray
• Handmade
• All Natural
• Fonts of vintage style - varying with simple and bold (i attached some photos)
Nice to have
• **MAYBE a very Simple Bone (see drawing) - very very thin.
Should not have
• 1. PAWS or cheap looking dog related items
• 2. No bright colors - truly prefer black and white or black with intention to print on plain pulp/brown paper (attached photo)
• 3. Over designed

```html
<!DOCTYPE html>
<html lang="en">
<head>
<meta charset="utf-8">
<title>Willow Bend Meadows – Fur Refresher Label</title>
<link rel="stylesheet" href="https://fonts.googleapis.com/css2?family=Dancing+Script:wght@500&family=Quicksand:wght@500;600&family=Fredoka:wght@600&display=swap">
<style>
  :root {
    --page: #f3f3f2;
    --label: #474547;
    --label-deep: #3a393b;
    --mint: #bfe0d3;
    --mint-text: #d3eadf;
    --white: #ffffff;
    --rule: #d9d9d9;
    --ridge: #55535a;
  }
  * { margin: 0; padding: 0; box-sizing: border-box; }
  html, body { width: 1200px; height: 2273px; overflow: hidden; }
  body { background: var(--page); position: relative; }

  .label {
    position: absolute;
    left: 100px; top: 536px;
    width: 1000px; height: 1200px;
    text-align: center;
    color: var(--white);
  }
  .label-frame { position: absolute; inset: 0; }

  .ridge-band {
    position: absolute;
    left: 90px; right: 90px; top: 205px; height: 90px;
    background: linear-gradient(180deg, var(--ridge) 0%, rgba(85,83,90,0) 100%);
    opacity: .55;
  }

  .brand-mark {
    position: absolute;
    left: 50%; top: 90px;
    transform: translateX(-50%);
    width: 420px;
    display: flex; flex-direction: column; align-items: center; gap: 22px;
  }
  .brand-mark-dot {
    width: 120px; height: 120px; border-radius: 50%;
    background: var(--white);
  }
  .brand-mark-name {
    font-family: "Quicksand", sans-serif;
    font-weight: 600;
    font-size: 44px; line-height: 1.15;
    color: var(--white);
  }

  .brand-script {
    position: absolute; left: 0; right: 0; top: 555px;
    font-family: "Dancing Script", cursive;
    font-weight: 500; font-size: 78px; line-height: 1;
  }
  .provisions {
    position: absolute; left: 0; right: 0; top: 665px;
    display: flex; justify-content: center; align-items: center; gap: 14px;
    font-family: "Quicksand", sans-serif;
    font-weight: 500; font-size: 42px; line-height: 1;
  }
  .provisions svg { width: 110px; height: 34px; }

  .rule {
    position: absolute; left: 210px; right: 210px; height: 3px;
    background: var(--rule);
  }
  .rule-top { top: 738px; }
  .rule-bottom { top: 910px; }

  .product-name {
    position: absolute; left: 0; right: 0; top: 762px;
    font-family: "Fredoka", sans-serif;
    font-weight: 600; font-size: 112px; line-height: 1.1;
    color: var(--mint-text);
    letter-spacing: 1px;
  }
  .claims {
    position: absolute; left: 0; right: 0; top: 940px;
    font-family: "Dancing Script", cursive;
    font-weight: 500; font-size: 62px; line-height: 1;
  }
  .established {
    position: absolute; left: 0; right: 0; top: 1030px;
    font-family: "Quicksand", sans-serif;
    font-weight: 500; font-size: 38px; line-height: 1;
  }
</style>
</head>
<body>
  <main class="label">
    <svg class="label-frame" viewBox="0 0 1000 1200" aria-hidden="true">
      <defs>
        <linearGradient id="label-fill" x1="0" y1="0" x2="0" y2="1">
          <stop offset="0" stop-color="#4b494b"/>
          <stop offset="1" stop-color="#3c3b3d"/>
        </linearGradient>
      </defs>
      <path d="M40 4 H960 A36 36 0 0 0 996 40 V1160 A36 36 0 0 0 960 1196 H40 A36 36 0 0 0 4 1160 V40 A36 36 0 0 0 40 4 Z"
            fill="url(#label-fill)" stroke="var(--mint)" stroke-width="8"/>
      <path d="M78 40 H922 A38 38 0 0 0 960 78 V1122 A38 38 0 0 0 922 1160 H78 A38 38 0 0 0 40 1122 V78 A38 38 0 0 0 78 40 Z"
            fill="none" stroke="var(--mint)" stroke-width="3"/>
    </svg>

    <div class="ridge-band" role="img" aria-label="Faint mountain ridge silhouette behind the brand mark"></div>

    <div class="brand-mark">
      <span class="brand-mark-dot"></span>
      <span class="brand-mark-name">Willow Bend Meadows Dog Camp</span>
    </div>

    <p class="brand-script">Willow Bend Meadows</p>
    <p class="provisions">
      <span>Grooming</span>
      <svg viewBox="0 0 110 34" aria-hidden="true">
        <g fill="var(--white)">
          <rect x="16" y="12" width="78" height="10" rx="3"/>
          <circle cx="12" cy="10" r="9"/><circle cx="12" cy="24" r="9"/>
          <circle cx="98" cy="10" r="9"/><circle cx="98" cy="24" r="9"/>
        </g>
      </svg>
      <span>Provisions</span>
    </p>

    <div class="rule rule-top"></div>
    <h1 class="product-name">Fur Refresher</h1>
    <div class="rule rule-bottom"></div>

    <p class="claims">hand made | all natural</p>
    <p class="established">*est 2005*</p>
  </main>
</body>
</html>
```